"Vine Hollow Excursions" is a top notch Santa Barbara County Wine Tour company.

We provide scenic, boutique and custom wine tours. I need the card to be clean and classy. I will provide our logo. I would like the logo to cover the back side of the card as an option and would like to see a couple color options other then our signature green and gold. I would like to see some creative options and let the designers come up with options.
I need cards for myself and my team. The final design should communicate "An authentic and boutique wine tour experience"
Please use my website for reference www.vinehollowexcursions.example

Target Market(s)

We have a wide range of clients from millennials to baby boomers

Industry/Entity Type

Tour

Contact Information for Business Card

Contact info:
Dale Marsh
805-218-6390
info@vinehollowexcursions.example
vinehollowexcursions.example

Colors

Designer to choose colors to be used in the design.

Requirements
Must have
• my logo
Nice to have
• *I would like to have the backside side with the logo and the company statement
• "An authentic and boutique wine tour experience" as an option.
• *I would also like to see what the designers can create!
• *I would like to see an option that incorporates or social: pixgram, rantly, journey guide
Should not have
• I do not want it too busy.

```html
<!DOCTYPE html>
<html lang="en">
<head>
<meta charset="utf-8">
<title>Vine Hollow Excursions – Business Card</title>
<link rel="stylesheet" href="https://fonts.googleapis.com/css2?family=Noto+Sans:wght@400;600&display=swap">
<style>
  :root {
    --backdrop: #4a403a;
    --card: #1b1b1b;
    --card-edge: #111111;
    --ink: #f2f2f2;
    --muted: #bdbdbd;
    --gold: #c9b38f;
    --green: #2f8a57;
    --rule: #6f6f6f;
  }
  * { box-sizing: border-box; margin: 0; padding: 0; }
  html, body { width: 1200px; height: 715px; overflow: hidden; }
  body {
    background: var(--backdrop);
    font-family: "Noto Sans", Arial, sans-serif;
    color: var(--ink);
    position: relative;
  }
  .card {
    position: absolute;
    top: 203px;
    width: 540px;
    height: 308px;
    background: var(--card);
    border: 1px solid var(--card-edge);
    box-shadow: 0 10px 28px rgba(0,0,0,.45);
  }
  .card--back { left: 40px; display: flex; flex-direction: column; align-items: center; justify-content: center; }
  .card--front { left: 620px; }

  /* back: brand + socials */
  .brand-name {
    font-size: 30px;
    font-weight: 400;
    letter-spacing: 2px;
    color: var(--ink);
    text-transform: uppercase;
    display: flex;
    align-items: center;
    gap: 12px;
  }
  .brand-dot { width: 14px; height: 14px; border-radius: 50%; background: var(--ink); flex: none; }
  .social-row {
    margin-top: 34px;
    display: flex;
    align-items: center;
    gap: 14px;
    font-size: 11px;
    color: var(--muted);
    letter-spacing: .5px;
  }
  .social-row .rule { width: 50px; height: 1px; background: var(--rule); }
  .social-row .sep { color: var(--rule); }

  /* front: contact side */
  .front-brand {
    position: absolute;
    left: 28px; top: 70px;
    width: 230px;
    text-align: center;
  }
  .front-brand .brand-name {
    font-size: 19px;
    letter-spacing: 1.5px;
    color: var(--gold);
    justify-content: center;
    flex-wrap: wrap;
    line-height: 1.4;
  }
  .front-brand .brand-dot { width: 12px; height: 12px; background: var(--green); }
  .divider {
    position: absolute;
    left: 278px; top: 62px;
    width: 1px; height: 150px;
    background: var(--rule);
  }
  .contact {
    position: absolute;
    left: 300px; top: 54px;
    right: 16px;
  }
  .contact-name { font-size: 17px; font-weight: 600; color: var(--green); letter-spacing: .5px; }
  .contact-title { font-size: 10px; color: var(--ink); margin-bottom: 10px; }
  .contact-list { list-style: none; }
  .contact-list li {
    display: flex; align-items: flex-start; gap: 8px;
    font-size: 11.5px; line-height: 1.3; margin-bottom: 6px;
  }
  .contact-list svg { width: 11px; height: 11px; flex: none; margin-top: 2px; fill: var(--green); }
  .tagline {
    position: absolute;
    left: 0; right: 0; bottom: 30px;
    display: flex; align-items: center; justify-content: center; gap: 14px;
    font-size: 11.5px; color: var(--ink);
  }
  .tagline .rule { width: 36px; height: 1px; background: var(--rule); }
</style>
</head>
<body>

<section class="card card--back">
  <div class="brand-name"><span class="brand-dot"></span>Vine Hollow Excursions</div>
  <div class="social-row">
    <span class="rule"></span>
    <span>facepage</span><span class="sep">•</span>
    <span>pixgram</span><span class="sep">•</span>
    <span>rantly</span><span class="sep">•</span>
    <span>journey guide</span>
    <span class="rule"></span>
  </div>
</section>

<section class="card card--front">
  <div class="front-brand">
    <div class="brand-name"><span class="brand-dot"></span>Vine Hollow Excursions</div>
  </div>
  <div class="divider"></div>
  <div class="contact">
    <p class="contact-name">Dale Marsh</p>
    <p class="contact-title">Title</p>
    <ul class="contact-list">
      <li>
        <svg viewBox="0 0 24 24" aria-hidden="true"><path d="M6.6 10.8a15 15 0 0 0 6.6 6.6l2.2-2.2c.3-.3.7-.4 1-.2 1.1.4 2.3.6 3.6.6.6 0 1 .4 1 1V20c0 .6-.4 1-1 1A17 17 0 0 1 3 4c0-.6.4-1 1-1h3.5c.6 0 1 .4 1 1 0 1.3.2 2.5.6 3.6.1.3 0 .7-.2 1z"/></svg>
        805-218-6390
      </li>
      <li>
        <svg viewBox="0 0 24 24" aria-hidden="true"><path d="M2 5h20v14H2z M2 5l10 8 10-8" fill="none" stroke="#2f8a57" stroke-width="2"/></svg>
        info@vinehollowexcursions.example
      </li>
      <li>
        <svg viewBox="0 0 24 24" aria-hidden="true"><circle cx="12" cy="12" r="9" fill="none" stroke="#2f8a57" stroke-width="2"/><path d="M3 12h18M12 3c3 3 3 15 0 18M12 3c-3 3-3 15 0 18" fill="none" stroke="#2f8a57" stroke-width="1.6"/></svg>
        www.vinehollowexcursions.example
      </li>
      <li>
        <svg viewBox="0 0 24 24" aria-hidden="true"><path d="M12 2a7 7 0 0 0-7 7c0 5 7 13 7 13s7-8 7-13a7 7 0 0 0-7-7zm0 9.5A2.5 2.5 0 1 1 12 6.5a2.5 2.5 0 0 1 0 5z"/></svg>
        <span>238 Vista Arroyo Lane<br>Santa Barbara, CA 93101</span>
      </li>
    </ul>
  </div>
  <p class="tagline"><span class="rule"></span>An authentic and boutique wine tour experience<span class="rule"></span></p>
</section>

</body>
</html>
```